Visitenkarten-Design für Familienunternehmen (Apotheke)
Zielgruppe
Wir sind ein Familienunternehmen und betreiben 4 Apotheken (alle eigene Namen: Lindenhof-Apotheke; Kessel-Apotheke; Apotheke St. Ottilien und VeroNova-Apotheke)
Wir beginnen, diese alle unter Sperling-Apotheken zusammenzufassen. www.sperling-apotheken.de (die VeroNova-Apotheke eröffnet erst am 1.1.18 neu, daher noch nicht online)
Konkret möchten wir für die Mitarbeiter der VeroNova-Apotheke Visitenkarten mit Porträt für Kunden erstellen.
Aktuell sind wir ca. 10 Mitarbeiter in dieser Apotheke. Ggf. möchten wir mittelfristig alle Mitarbeiter aller Apotheken (ca. 50-60) mit Visitenkarten ausstatten.
Aufgabenstellung
Wir haben vor Jahren selbst laienhaft eine Visitenkarte erstellt
Ich habe gegoogelt und andere Beispiele mit Porträt gefunden.
Wir suchen eine Visitenkarte, die sowohl das Logo VeroNova-Apotheke inkl. Adresse, Telefonnummer etc. hat (kann auch optisch verschoben werden - oben Logo - unten Adresse o.ä) , den Namen des Mitarbeitern und Beruf (Apothekerin o.ä.) und 2-3 Schlagwörter/Schlagsätze zu der Qualifikation des Mitarbeiters.
(die VeroNova-Apotheke hat eine Spezialzertifizierung 'Wiegensichere Offizin' und darf daher auch das Logo Wiegensichere Offizin nutzen. Eventuell gibt es die Möglichkeit dieses auch - nicht konkurrierend - neben dem Hauptlogo VeroNova-Apotheke unterzubringen)
unten gerne 'Sperling-Apotheken' o.ä. als Dachmarke
Mutter-Kind-Expertin (Zertifizierung Wiegensichere Offizin)
Fachberaterin für Darmgesundheit
!! Seriös, weniger verspielt. Druckbar für Druckwerk24, wir nehmen gerne Tipps zu Papier und Stärke an!
Ziel: Klares Design, wo einfach der Kopf des Mitarbeiters gewechselt werden kann und die Qualifikation, um für alle Mitarbeiter gleiche CI zu erstellen

```html
<!DOCTYPE html>
<html lang="de">
<head>
<meta charset="utf-8">
<title>Visitenkarte VeroNova-Apotheke</title>
<link rel="stylesheet" href="https://fonts.googleapis.com/css2?family=Open+Sans:ital,wght@0,400;0,600;0,700;1,600&display=swap">
<style>
  :root {
    --bg: #ececec;
    --card: #ffffff;
    --ink: #1c1c1c;
    --grey: #9a9a9a;
    --red: #e0251b;
    --pink: #ef7a8c;
    --pink-soft: #f6b3bd;
    --brown: #6b3a2a;
    --tan: #d9b98c;
    --sky: #4fb6e6;
  }
  * { box-sizing: border-box; margin: 0; padding: 0; }
  html, body { width: 1200px; height: 800px; overflow: hidden; }
  body {
    background: var(--bg);
    font-family: "Open Sans", Arial, sans-serif;
    color: var(--ink);
    position: relative;
  }
  .card {
    position: absolute;
    top: 235px;
    width: 510px;
    height: 330px;
    background: var(--card);
    box-shadow: 0 14px 34px rgba(0,0,0,.12);
    overflow: hidden;
  }
  .card--info { left: 60px; }
  .card--brand { left: 630px; }

  /* info side */
  .contact {
    position: absolute; left: 34px; top: 40px;
    font-size: 10.5px; line-height: 1.65;
  }
  .contact .link { color: var(--red); }
  .portrait {
    position: absolute; right: 0; top: 0;
    width: 180px; height: 190px;
    background: linear-gradient(160deg, #8a6a58, #c9a493 55%, #e8e3de);
  }
  .corner {
    position: absolute; right: 0; top: 0;
  }
  .brand-mark {
    position: absolute; left: 34px; top: 190px;
    display: flex; align-items: center; gap: 8px;
    font-size: 19px; font-weight: 700;
  }
  .brand-mark .dot {
    width: 10px; height: 10px; border-radius: 50%; background: var(--red);
  }
  .person {
    position: absolute; left: 34px; bottom: 34px;
  }
  .person__name { font-size: 22px; font-weight: 700; letter-spacing: .2px; }
  .person__branch { font-size: 14px; font-weight: 600; font-style: italic; color: var(--red); margin-top: 2px; }
  .person__role { font-size: 13px; color: var(--grey); margin-top: 2px; }

  /* brand side */
  .artwork {
    position: absolute; left: 70px; top: 40px;
    width: 370px; height: 250px;
    background: linear-gradient(135deg, var(--sky) 0 6%, var(--pink-soft) 6% 35%, var(--pink) 55%, var(--brown) 80%, var(--tan));
    border-radius: 8px;
  }
  .brand-name {
    position: absolute; left: 250px; top: 64px;
    font-size: 22px; font-weight: 700; color: #ffffff;
    line-height: 1.05;
  }
</style>
</head>
<body>

  <section class="card card--info" aria-label="Rückseite mit Kontaktdaten">
    <div class="contact">
      <div>Lindenallee 14, 52234 Feldhausen · Tel. 02405 / 98 31 20</div>
      <div>Fax 02405 / 98 31 21 · Mo–Sa geöffnet</div>
      <div class="link">info@veronova-apotheke.de</div>
      <div class="link">www.sperling-apotheken.de</div>
      <div>www.wiegensichere-offizin.de</div>
    </div>

    <div class="portrait" role="img" aria-label="Porträtfoto der Mitarbeiterin"></div>
    <svg class="corner" width="70" height="70" viewBox="0 0 70 70" aria-hidden="true">
      <polyline points="10,0 70,0 70,60" fill="none" stroke="var(--red)" stroke-width="12"/>
    </svg>

    <div class="brand-mark"><span class="dot"></span><span>VeroNova-Apotheke</span></div>

    <div class="person">
      <div class="person__name">Jana Wehrstedt</div>
      <div class="person__branch">Apotheke St. Ottilien</div>
      <div class="person__role">Apothekerin und andere Qualifikation</div>
    </div>
  </section>

  <section class="card card--brand" aria-label="Vorderseite">
    <div class="artwork" role="img" aria-label="Illustration: rosa Band um eine braune Arzneiflasche"></div>
    <div class="brand-name">VeroNova-<br>Apotheke</div>
  </section>

</body>
</html>
```